Parkinson's Disease Progression

Visually describe the rate of Parkinson progression in the first 15 years following diagnosis. Title: "Patient-Perceived Progression of Parkinsonism"

The attached figure names "meanqol" is the curve that should serve as the basis of this graphic. Everything else-- color, labels, font, etc. describe this curve.
Thank you!

Target Market(s)

People with Parkisnon's Disease, neurologists, family members.

Font styles to use
Sans Serif

Requirements
Must have
• Must have the lines going through these exact numbers
Excellent -- 502
Very good- 661
Good- 895
Fair- 1268
Poor- 1655

LABELS:
Title: "Patient-Perceived Progression of Parkinsonism"
"SWI-TC (Self-Logged Wellbeing Index for Tremor Conditions)" should be the label on the left.
"Quality of Life" should be the label on the right
"Years Since Diagnosis" should be the label on the bottom
Nice to have
• A color scheme that goes from GOOD (low numbers) to BAD (high numbers).

Easy to read (elderly)

```html
<!DOCTYPE html>
<html lang="en">
<head>
<meta charset="utf-8">
<title>Patient-Perceived Progression of Parkinsonism</title>
<link rel="stylesheet" href="https://fonts.googleapis.com/css2?family=Lato:wght@700;900&display=swap">
<style>
  :root {
    --page: #ffffff;
    --panel: #d4effc;
    --ink: #0a6333;
    --poor: #04305f;
    --fair: #03528f;
    --good: #1a8ac8;
    --very-good: #4ecff9;
    --excellent: #a5ebfc;
    --curve: #f5ec00;
    --band-ink: #ffffff;
    --tick: #1b1b1b;
  }
  html, body {
    margin: 0;
    padding: 0;
    width: 1200px;
    height: 960px;
    overflow: hidden;
    background: var(--page);
    font-family: "Lato", Arial, sans-serif;
  }
  .canvas {
    position: relative;
    width: 1200px;
    height: 960px;
  }
  .title-band {
    position: absolute;
    left: 72px;
    top: 66px;
    width: 1055px;
    height: 111px;
    background: var(--panel);
    display: flex;
    align-items: center;
    justify-content: center;
  }
  .title-band h1 {
    margin: 0;
    color: var(--ink);
    font-weight: 900;
    font-size: 33px;
    letter-spacing: -0.3px;
    text-transform: uppercase;
  }
  .chart-panel {
    position: absolute;
    left: 72px;
    top: 182px;
    width: 1056px;
    height: 700px;
    background: var(--panel);
  }
  .chart {
    position: absolute;
    left: 0;
    top: 0;
  }
  .axis-value { fill: var(--ink); font-weight: 900; font-size: 21px; }
  .axis-title { fill: var(--ink); font-weight: 900; font-size: 24px; }
  .axis-subtitle { fill: var(--ink); font-weight: 700; font-size: 13px; }
  .band-label { fill: var(--band-ink); font-weight: 900; font-size: 24px; }
  .tick { stroke: var(--tick); stroke-width: 1.6; }
  .curve-mean { fill: none; stroke: var(--curve); stroke-width: 3.2; stroke-linecap: round; }
  .curve-bound { fill: none; stroke: #ffffff; stroke-width: 1.8; stroke-dasharray: 3 4; stroke-linecap: round; }
</style>
</head>
<body>
<div class="canvas">
  <header class="title-band">
    <h1>Patient-Perceived Progression of Parkinsonism</h1>
  </header>
  <section class="chart-panel"></section>

  <svg class="chart" width="1200" height="960" viewBox="0 0 1200 960" aria-label="Line chart of SWI-TC score over 15 years since diagnosis">
    <!-- quality bands -->
    <rect x="267" y="231" width="771" height="70" fill="var(--poor)"/>
    <rect x="267" y="301" width="771" height="135" fill="var(--fair)"/>
    <rect x="267" y="436" width="771" height="83" fill="var(--good)"/>
    <rect x="267" y="519" width="771" height="59" fill="var(--very-good)"/>
    <rect x="267" y="578" width="771" height="182" fill="var(--excellent)"/>

    <g text-anchor="middle">
      <text class="band-label" x="592" y="277">POOR-1655</text>
      <text class="band-label" x="592" y="380">FAIR-1268</text>
      <text class="band-label" x="592" y="464">GOOD-895</text>
      <text class="band-label" x="592" y="561">VERY GOOD - 661</text>
      <text class="band-label" x="592" y="678">EXCELLENT- 502</text>
    </g>

    <!-- y axis -->
    <g class="tick">
      <line x1="243" y1="253" x2="262" y2="253"/>
      <line x1="243" y1="326" x2="262" y2="326"/>
      <line x1="243" y1="398" x2="262" y2="398"/>
      <line x1="243" y1="470" x2="262" y2="470"/>
      <line x1="243" y1="543" x2="262" y2="543"/>
      <line x1="243" y1="615" x2="262" y2="615"/>
      <line x1="243" y1="688" x2="262" y2="688"/>
    </g>
    <g text-anchor="end">
      <text class="axis-value" x="231" y="260">1600</text>
      <text class="axis-value" x="231" y="333">1200</text>
      <text class="axis-value" x="231" y="405">1000</text>
      <text class="axis-value" x="231" y="477">800</text>
      <text class="axis-value" x="231" y="550">600</text>
      <text class="axis-value" x="231" y="622">400</text>
      <text class="axis-value" x="231" y="695">200</text>
    </g>

    <!-- x axis -->
    <g class="tick">
      <line x1="314" y1="762" x2="314" y2="779"/>
      <line x1="534" y1="762" x2="534" y2="779"/>
      <line x1="754" y1="762" x2="754" y2="779"/>
      <line x1="973" y1="762" x2="973" y2="779"/>
    </g>
    <g text-anchor="middle">
      <text class="axis-value" x="314" y="812">0</text>
      <text class="axis-value" x="534" y="812">5</text>
      <text class="axis-value" x="756" y="812">10</text>
      <text class="axis-value" x="975" y="812">15</text>
      <text class="axis-title" x="640" y="853">YEARS SINCE DIAGNOSIS</text>
    </g>

    <!-- axis titles -->
    <text class="axis-title" text-anchor="middle" transform="translate(131 480) rotate(-90)">SWI-TC</text>
    <text class="axis-subtitle" text-anchor="middle" transform="translate(151 480) rotate(-90)">(Self-Logged Wellbeing Index for Tremor Conditions)</text>
    <text class="axis-title" text-anchor="middle" transform="translate(1083 480) rotate(-90)">QUALITY OF LIFE</text>

    <!-- progression curves -->
    <path class="curve-bound" d="M317 564 C340 560 360 553 372 549 C405 536 430 524 456 513 C480 500 500 489 522 487 C560 479 600 484 624 479 C645 475 660 470 672 465 C705 450 730 437 750 426 C775 410 795 400 810 393 C845 377 875 370 900 357 C930 343 955 328 973 315"/>
    <path class="curve-bound" d="M317 636 C340 612 365 590 390 573 C420 553 450 535 480 522 C500 513 520 508 540 507 C580 503 615 505 636 501 C655 497 668 492 678 486 C705 473 730 461 756 450 C790 434 815 420 840 414 C870 407 895 405 912 408 C935 410 955 412 973 414"/>
    <path class="curve-mean" d="M317 600 C335 588 348 579 362 570 C385 555 400 546 420 535 C445 522 465 510 480 505 C500 498 515 498 534 497 C570 494 600 496 618 492 C635 489 648 485 660 480 C695 465 725 452 756 438 C785 422 805 408 828 399 C855 388 880 382 900 378 C930 371 955 367 973 365"/>
  </svg>
</div>
</body>
</html>
```